Create Social Media design templates for Online-Education-Startup

We are an online platform for pupils who provide group courses and on demand individual tutroing lessons. Our core values are personalisation, family and success. We need a holistic social media design concept which includes nine possible layouts for Instagram posts which reflect our values and promote not only our offerings and special deals but also support in building our brand image (for example: telling company history, daily news, funny facts, getting to know the team etc.).
Additionally, we need design elements for our YouTube channel:
-Videocover
-Cover Image for the channel

Our main colour is orange (RGB-Code: 255;105;31) and additional colours white, black, and grey. For the reference have a look at our website: www.lernquorvo.de.

Target Market(s)

We want to attract customers to our online tutoring courses and build a brand.

Industry/Entity Type

Education / Tutoring

Font styles to use
Sans Serif

Requirements
Must have
• Familiarize yourself with the style of our website. The designs should fit as well as possible.

```html
<!DOCTYPE html>
<html lang="en">
<head>
<meta charset="utf-8">
<title>Lernquorvo – Social Media Templates</title>
<link rel="stylesheet" href="https://fonts.googleapis.com/css2?family=Outfit:wght@300;400;500;600;700;800&display=swap">
<style>
  :root {
    --orange: #ff691f;
    --orange-deep: #f25a0f;
    --orange-soft: #ffe3d6;
    --cream: #fde9a6;
    --white: #ffffff;
    --ink: #1d1d1d;
    --grey: #5f5f5f;
    --page: #f3f3f3;
  }
  * { margin: 0; padding: 0; box-sizing: border-box; }
  html, body { width: 673px; height: 1200px; overflow: hidden; background: var(--page); }
  body { position: relative; font-family: "Outfit", sans-serif; color: var(--ink); }

  .section-title { position: absolute; left: 26px; font-size: 22px; font-weight: 500; color: var(--grey); letter-spacing: .2px; }
  .section-title--instagram { top: 44px; }
  .section-title--youtube { top: 766px; }

  .post { position: absolute; width: 200px; height: 200px; overflow: hidden; }
  .post--white { background: var(--white); }
  .post--orange { background: var(--orange); color: var(--white); }
  .col-1 { left: 26px; } .col-2 { left: 236px; } .col-3 { left: 446px; }
  .row-1 { top: 85px; } .row-2 { top: 297px; } .row-3 { top: 509px; }

  .brand { position: absolute; left: 10px; top: 10px; display: flex; align-items: center; gap: 3px; z-index: 3; }
  .brand__dot { width: 14px; height: 14px; border-radius: 50%; border: 1.5px solid var(--orange); }
  .post--orange .brand__dot { border-color: var(--white); }
  .brand__text { line-height: 1.1; font-size: 4.6px; }
  .brand__name { font-weight: 700; display: block; }
  .brand__sub { font-weight: 400; display: block; }
  .post--orange .brand__text { color: var(--white); }
  .post-url { position: absolute; right: 10px; top: 13px; font-size: 4.8px; z-index: 3; }
  .post--orange .post-url { color: var(--white); }

  .photo { position: absolute; }

  /* join steps */
  .join__block { position: absolute; left: 0; top: 72px; width: 72px; height: 104px; background: var(--orange); border-radius: 0 14px 0 0; }
  .join__photo { left: 0; top: 36px; width: 72px; height: 140px; border-radius: 0 22px 14px 0; background: linear-gradient(180deg, #e9eef2, #cfd6dc); }
  .join__title { position: absolute; left: 83px; top: 60px; font-size: 13px; font-weight: 700; color: var(--orange); line-height: 1.15; }
  .join__steps { position: absolute; left: 82px; top: 96px; list-style: none; }
  .join__steps li { display: flex; gap: 5px; margin-bottom: 4.3px; }
  .join__num { width: 11px; height: 11px; border-radius: 50%; background: var(--orange-soft); color: var(--orange); font-size: 4.3px; display: flex; align-items: center; justify-content: center; flex-shrink: 0; }
  .join__steps strong { font-size: 4.2px; font-weight: 600; display: block; }
  .join__steps span { font-size: 4px; color: var(--grey); display: block; line-height: 1.3; }

  /* trial */
  .trial__news { position: absolute; left: 14px; top: 38px; font-size: 45px; font-weight: 800; color: var(--orange-deep); line-height: .95; letter-spacing: 1px; }
  .trial__card { position: absolute; left: 33px; top: 62px; width: 135px; height: 86px; background: var(--white); border-radius: 10px 22px 10px 10px; }
  .trial__title { position: absolute; left: 18px; top: 12px; font-size: 19px; font-weight: 800; color: var(--orange); line-height: 1; }
  .trial__text { position: absolute; left: 19px; top: 55px; font-size: 5.6px; color: var(--ink); line-height: 1.35; }
  .trial__pill { position: absolute; left: 42px; top: 138px; width: 92px; height: 19px; background: var(--white); border-radius: 10px; box-shadow: 0 2px 4px rgba(0,0,0,.15); display: flex; align-items: center; justify-content: space-between; padding: 0 2px 0 9px; font-size: 8px; font-weight: 700; color: var(--orange); }
  .trial__search { width: 15px; height: 15px; border-radius: 50%; background: var(--orange); display: flex; align-items: center; justify-content: center; }

  /* fun fact */
  .fact__tag { position: absolute; left: 75px; top: 33px; width: 47px; height: 15px; background: var(--white); color: var(--orange); border-radius: 6px; font-size: 7.5px; display: flex; align-items: center; justify-content: center; }
  .fact__lead { position: absolute; left: 0; right: 0; top: 62px; text-align: center; font-size: 4.8px; line-height: 1.35; }
  .fact__lead strong { font-weight: 600; }
  .fact__big { position: absolute; left: 0; right: 0; top: 72px; text-align: center; font-size: 46px; font-weight: 800; color: var(--cream); letter-spacing: -1px; line-height: 1; }
  .fact__foot { position: absolute; left: 0; right: 0; top: 121px; text-align: center; font-size: 5px; line-height: 1.35; }
  .fact__photo { left: 0; top: 142px; width: 200px; height: 58px; background: linear-gradient(180deg, #f5f5f5, #dedede); }

  /* online tutoring */
  .online__photo { left: 0; top: 0; width: 200px; height: 200px; background: linear-gradient(135deg, #b9b4ae, #6f6a66 60%, #3b3a3a); }
  .online__card { position: absolute; left: 31px; top: 40px; width: 138px; height: 138px; border-radius: 9px; background: rgba(255,105,31,.9); }
  .online__title { position: absolute; left: 15px; top: 15px; font-size: 13px; font-weight: 700; line-height: 1.18; }
  .online__rule { position: absolute; left: 17px; top: 68px; width: 15px; height: 1px; background: var(--white); }
  .online__text { position: absolute; left: 17px; top: 99px; width: 80px; font-size: 3.9px; line-height: 1.4; }

  /* testimonial */
  .quote__photo { left: 0; top: 43px; width: 108px; height: 63px; border-radius: 0 32px 32px 0; background: linear-gradient(135deg, #c9b79b, #e8c74f 70%, #b88a3b); }
  .quote__badge { position: absolute; left: 126px; top: 61px; width: 80px; height: 26px; background: var(--cream); border-radius: 13px 0 0 13px; color: var(--orange); padding: 5px 0 0 14px; font-size: 4.8px; line-height: 1.35; }
  .quote__badge strong { font-weight: 700; display: block; }
  .quote__lead { position: absolute; left: 30px; top: 118px; font-size: 5px; line-height: 1.35; }
  .quote__mark { position: absolute; left: 29px; top: 131px; font-size: 17px; font-weight: 800; color: var(--cream); line-height: 1; }
  .quote__title { position: absolute; left: 45px; top: 130px; font-size: 19px; font-weight: 700; line-height: 1; }
  .quote__foot { position: absolute; left: 45px; top: 175px; font-size: 5px; line-height: 1.35; }

  /* concept */
  .concept__top { position: absolute; left: 19px; top: 40px; font-size: 12.5px; font-weight: 300; line-height: .95; }
  .concept__top strong, .concept__bottom strong { display: block; font-weight: 700; color: var(--orange); }
  .concept__photo { left: 19px; top: 71px; width: 162px; height: 81px; border-radius: 6px; background: linear-gradient(135deg, #5d6773, #98a3af 55%, #d7d4cf); }
  .concept__bottom { position: absolute; left: 98px; top: 154px; font-size: 12.5px; font-weight: 300; line-height: .95; }

  /* team */
  .team__photo { left: 104px; top: 27px; width: 96px; height: 173px; border-radius: 46px 46px 0 0; background: linear-gradient(180deg, #eed6c1, #f3f3f3 55%, #e9e9e9); }
  .team__kicker { position: absolute; left: 10px; top: 61px; font-size: 7.5px; font-weight: 300; }
  .team__name { position: absolute; left: 9px; top: 70px; font-size: 29px; font-weight: 800; line-height: .97; letter-spacing: -.3px; }
  .team__role { position: absolute; left: 10px; top: 133px; font-size: 7.2px; font-weight: 300; }

  /* sport */
  .sport__title { position: absolute; left: 11px; top: 34px; font-size: 19px; font-weight: 800; color: var(--orange); line-height: 1; }
  .sport__text { position: absolute; left: 11px; top: 78px; width: 90px; font-size: 4px; color: var(--grey); line-height: 1.35; }
  .sport__photo { left: 48px; top: 80px; width: 142px; height: 120px; border-radius: 60px 60px 0 0; background: linear-gradient(180deg, #d8c0a6, #f1eeea 60%, #e4e2df); }

  /* youtube cover */
  .cover { position: absolute; left: 26px; top: 805px; width: 620px; height: 349px; background: var(--orange); color: var(--white); overflow: hidden; }
  .cover__board { left: 433px; top: 0; width: 187px; height: 349px; background: linear-gradient(160deg, #e4e1dc, #c9c6c1); }
  .cover__host { left: 335px; top: 30px; width: 285px; height: 319px; border-radius: 140px 140px 0 0; background: linear-gradient(180deg, #f0d2bb, #f6f6f6 45%, #e6e6e6); }
  .cover__brand { position: absolute; left: 46px; top: 32px; display: flex; align-items: center; gap: 5px; }
  .cover__brand .brand__dot { width: 35px; height: 35px; border: 3px solid var(--white); }
  .cover__brand .brand__text { font-size: 12px; line-height: 1.15; }
  .cover__headline { position: absolute; left: 50px; top: 84px; font-size: 50px; font-weight: 800; line-height: 1.09; letter-spacing: -.5px; }
  .cover__rule { position: absolute; left: 51px; top: 262px; width: 1.5px; height: 55px; background: var(--cream); }
  .cover__with { position: absolute; left: 69px; top: 262px; font-size: 19px; font-weight: 300; }
  .cover__with strong { font-weight: 600; color: var(--cream); }
  .cover__role { position: absolute; left: 70px; top: 289px; font-size: 11.5px; line-height: 1.3; }
</style>
</head>
<body>

<h2 class="section-title section-title--instagram">Instagram Content</h2>

<!-- How to join -->
<article class="post post--white col-1 row-1">
  <div class="brand"><span class="brand__dot"></span><span class="brand__text"><span class="brand__name">Lernquorvo</span><span class="brand__sub">Bildungsinstitut</span></span></div>
  <span class="post-url">lernquorvo.de</span>
  <div class="join__block"></div>
  <div class="photo join__photo" role="img" aria-label="Portrait of the founder in a white shirt"></div>
  <h3 class="join__title">How to join<br>Lernquorvo?</h3>
  <ol class="join__steps">
    <li><span class="join__num">01</span><div><strong>Starting signal</strong><span>Register and secure your free trial lesson.</span></div></li>
    <li><span class="join__num">02</span><div><strong>Catching up together</strong><span>Together with your trainer you will catch up.</span></div></li>
    <li><span class="join__num">03</span><div><strong>Extend your lead</strong><span>Regularity is the key to your success.</span></div></li>
    <li><span class="join__num">04</span><div><strong>Final spurt</strong><span>Don't lose your nerve now, prepare<br>specifically for your exam.</span></div></li>
  </ol>
</article>

<!-- Free trial -->
<article class="post post--orange col-2 row-1">
  <div class="brand"><span class="brand__dot"></span><span class="brand__text"><span class="brand__name">Lernquorvo</span><span class="brand__sub">Bildungsinstitut</span></span></div>
  <span class="post-url">lernquorvo.de</span>
  <div class="trial__news" aria-hidden="true">NEWS<br>NEWS<br>NEWS</div>
  <div class="trial__card">
    <h3 class="trial__title">Free Trial<br>Lesson</h3>
    <p class="trial__text">Get afree trial lesson!<br>No subscription!</p>
  </div>
  <div class="trial__pill">lernquorvo.de
    <span class="trial__search"><svg width="8" height="8" viewBox="0 0 10 10"><circle cx="4" cy="4" r="3" fill="none" stroke="#fff" stroke-width="1.3"/><line x1="6.2" y1="6.2" x2="9" y2="9" stroke="#fff" stroke-width="1.3" stroke-linecap="round"/></svg></span>
  </div>
</article>

<!-- Student at whiteboard -->
<article class="post post--white col-3 row-1">
  <div class="photo" style="left:0;top:0;width:200px;height:200px;background:linear-gradient(135deg,#eceff1,#ffffff 50%,#ff8a4d);" role="img" aria-label="Student writing on a whiteboard with an orange brand swirl"></div>
  <div class="brand"><span class="brand__dot"></span><span class="brand__text"><span class="brand__name">Lernquorvo</span><span class="brand__sub">Bildungsinstitut</span></span></div>
  <span class="post-url">lernquorvo.de</span>
</article>

<!-- Fun fact -->
<article class="post post--orange col-1 row-2">
  <div class="brand"><span class="brand__dot"></span><span class="brand__text"><span class="brand__name">Lernquorvo</span><span class="brand__sub">Bildungsinstitut</span></span></div>
  <span class="post-url">lernquorvo.de</span>
  <span class="fact__tag">Fun Fact!</span>
  <p class="fact__lead"><strong>Students who attend tutoring sessions</strong><br>regularly can improve their grades by up to</p>
  <p class="fact__big">30%</p>
  <p class="fact__foot">Personalized attention and extra practice<br>make learning more effective and fun.</p>
  <div class="photo fact__photo" role="img" aria-label="Laptop showing the website next to a coffee cup on a desk"></div>
</article>

<!-- Online tutoring -->
<article class="post post--orange col-2 row-2">
  <div class="photo online__photo" role="img" aria-label="Group of students gathered around a table"></div>
  <div class="brand"><span class="brand__dot"></span><span class="brand__text"><span class="brand__name">Lernquorvo</span><span class="brand__sub">Bildungsinstitut</span></span></div>
  <span class="post-url">lernquorvo.de</span>
  <div class="online__card">
    <h3 class="online__title">Online tutoring<br>distinguishes<br>Lernquorvo</h3>
    <span class="online__rule"></span>
    <p class="online__text">The inexhaustible innovative possibilities to impart and increase knowledge are what drives us every day for you.</p>
  </div>
</article>

<!-- Testimonial -->
<article class="post post--orange col-3 row-2">
  <div class="brand"><span class="brand__dot"></span><span class="brand__text"><span class="brand__name">Lernquorvo</span><span class="brand__sub">Bildungsinstitut</span></span></div>
  <span class="post-url">lernquorvo.de</span>
  <div class="photo quote__photo" role="img" aria-label="Smiling student holding books in front of a school building"></div>
  <div class="quote__badge"><strong>Mira</strong>Highschool Student</div>
  <p class="quote__lead">The tutoring here has really helped<br>me improve my grades.</p>
  <span class="quote__mark">”</span>
  <h3 class="quote__title">The teachers<br>are great</h3>
  <p class="quote__foot">and always ready to explain things<br>clearly. I highly recommend this center!</p>
</article>

<!-- Concept -->
<article class="post post--white col-1 row-3">
  <div class="brand"><span class="brand__dot"></span><span class="brand__text"><span class="brand__name">Lernquorvo</span><span class="brand__sub">Bildungsinstitut</span></span></div>
  <span class="post-url">lernquorvo.de</span>
  <p class="concept__top">Our tutoring concept<strong>prepares you</strong></p>
  <div class="photo concept__photo" role="img" aria-label="Girl in an online lesson with a tutor on a laptop"></div>
  <p class="concept__bottom"><strong>step by step</strong>for your goal.</p>
</article>

<!-- Team -->
<article class="post post--orange col-2 row-3">
  <div class="brand"><span class="brand__dot"></span><span class="brand__text"><span class="brand__name">Lernquorvo</span><span class="brand__sub">Bildungsinstitut</span></span></div>
  <span class="post-url">lernquorvo.de</span>
  <div class="photo team__photo" role="img" aria-label="Portrait of the English teacher in a white t-shirt"></div>
  <p class="team__kicker">Meet out team!</p>
  <h3 class="team__name">Clara<br>Weiss</h3>
  <p class="team__role">English Teacher</p>
</article>

<!-- Sport -->
<article class="post post--white col-3 row-3">
  <div class="brand"><span class="brand__dot"></span><span class="brand__text"><span class="brand__name">Lernquorvo</span><span class="brand__sub">Bildungsinstitut</span></span></div>
  <span class="post-url">lernquorvo.de</span>
  <h3 class="sport__title">Our sport is<br>online tutoring.</h3>
  <p class="sport__text">Our goal is your graduation, whether it's high school diploma, intermediate school diploma or qualification. Our tutoring concept is exactly what you need.</p>
  <div class="photo sport__photo" role="img" aria-label="Two tutors looking at a tablet together"></div>
</article>

<h2 class="section-title section-title--youtube">Youtube Cover</h2>

<section class="cover">
  <div class="photo cover__board" role="img" aria-label="Chalk wall full of handwritten math formulas"></div>
  <div class="photo cover__host" role="img" aria-label="Founder in a white shirt and round glasses"></div>
  <div class="cover__brand"><span class="brand__dot"></span><span class="brand__text"><span class="brand__name">Lernquorvo</span><span class="brand__sub">Bildungsinstitut</span></span></div>
  <h1 class="cover__headline">Top Tips<br>for School<br>Success!</h1>
  <span class="cover__rule"></span>
  <p class="cover__with">with <strong>Jonas Brenner</strong></p>
  <p class="cover__role">Founder Lernquorvo and Professional<br>Tutor (Mathematics, Physics, Economics)</p>
</section>

</body>
</html>
```